I am a health and wellness guru. I am looking to make a website. Nothing too extensive but something to just promote on my socials and sell the info I know as digital assets. I will sell my daily workout as a monthly payment, and they will get updates on what I do daily... As well as a pdf of my day and a guide to a healthy lifestyle. I may offer meal plans and coaching as well. It will be called a venture brightpath and then offer those things. my Instagram @marlon_tibbet you can see kinda my vibe off stuff. I want a clean aesthetic look and simple. Whatever photos you reccoment ill provide when I pick a winning design

Target Market(s)

people who want to buy access to my way of life

Coding

Font styles to use
Serif
Sans Serif

Requirements
Must have
• Venture Brightpath by Marlon Tibbet
Nice to have
• About, plans to buy, why health and wellness is important. (exsposure to subnlight, ice baht, sauna, daily movement, whole foods)

```html
<!DOCTYPE html>
<html lang="en">
<head>
<meta charset="utf-8">
<title>Venture Brightpath – Fitness Plans</title>
<link href="https://fonts.googleapis.com/css2?family=Oswald:wght@500;600&family=Open+Sans:wght@400;600;700&display=swap" rel="stylesheet">
<style>
  :root{
    --hero-dark:#1b1b1d;
    --hero-red:#5a1d1a;
    --white:#ffffff;
    --ink:#2a2a2a;
    --muted:#6f6f6f;
    --teal:#3cc3a0;
    --red:#d6483b;
    --price-bg:#e6efec;
    --line:#e4e4e4;
    --page:#f5f5f5;
  }
  *{box-sizing:border-box;margin:0;padding:0}
  html,body{width:744px;height:1200px;overflow:hidden}
  body{font-family:"Open Sans",Arial,sans-serif;color:var(--ink);background:var(--white);position:relative}

  .hero{position:absolute;left:0;top:0;width:744px;height:242px;overflow:hidden}
  .hero-photo{position:absolute;inset:0;background:
      radial-gradient(ellipse 180px 220px at 330px 150px,#6b5a52 0%,rgba(60,45,40,.6) 45%,transparent 75%),
      linear-gradient(90deg,var(--hero-red) 0%,#2a1614 35%,var(--hero-dark) 60%,#3a2522 100%)}
  .account{position:absolute;right:62px;top:6px;font-size:10px;color:var(--white);display:flex;gap:5px;align-items:center}
  .site-nav{position:absolute;left:68px;right:68px;top:24px;height:40px;display:flex;align-items:center}
  .brand{color:var(--white);font-weight:600;line-height:1.15}
  .brand-name{font-size:15px;letter-spacing:1.5px}
  .brand-by{font-size:11px;padding-left:60px}
  .nav-links{display:flex;gap:26px;margin-left:auto;margin-right:26px;font-size:11px;color:var(--white)}
  .btn{display:inline-block;background:var(--teal);color:var(--white);font-weight:700;border-radius:20px;text-align:center;text-transform:uppercase}
  .btn-contact{font-size:11px;padding:9px 14px}
  .hero-title{position:absolute;left:68px;top:112px;font-family:"Oswald",Impact,sans-serif;font-weight:600;font-size:40px;line-height:1.08;color:var(--white);letter-spacing:.5px}

  .intro{position:absolute;left:150px;width:444px;top:290px;text-align:center;font-size:10px;line-height:1.7;color:var(--muted)}

  .plan{position:absolute;width:190px;background:var(--white);border-radius:8px;box-shadow:0 4px 14px rgba(0,0,0,.12);text-align:center;padding-top:18px}
  .plan h2{font-size:19px;font-weight:700}
  .plan .sessions{font-size:12px;margin-top:2px}
  .price{margin-top:14px;background:var(--price-bg);padding:10px 0;font-size:11px}
  .price strong{font-size:22px;font-weight:700;margin-right:3px}
  .plan.featured .price{background:var(--red);color:var(--white)}
  .features{list-style:none;text-align:left;padding:12px 14px 0 18px}
  .features li{position:relative;padding-left:13px;font-size:9.5px;line-height:1.35;margin-bottom:9px;color:var(--ink)}
  .features li svg{position:absolute;left:0;top:3px}
  .btn-buy{font-size:10px;padding:8px 16px;margin:6px 0 20px}

  .signup{position:absolute;left:0;top:816px;width:744px;height:120px;background:var(--red);text-align:center}
  .signup h2{font-family:"Oswald",Impact,sans-serif;font-weight:600;font-size:33px;color:var(--white);margin-top:20px;letter-spacing:.5px}
  .btn-register{font-size:11px;padding:9px 24px;margin-top:12px}

  .site-footer{position:absolute;left:0;top:936px;width:744px;height:264px;background:var(--white)}
  .footer-brand{position:absolute;left:68px;top:70px;color:var(--ink)}
  .footer-brand .brand-name{font-size:20px}
  .footer-brand .brand-by{font-size:14px;padding-left:80px}
  .footer-col{position:absolute;top:70px;font-size:10px;line-height:1.75}
  .footer-col h3{font-size:12px;font-weight:700;margin-bottom:6px}
  .links{left:372px}
  .contact{left:524px}
  .contact p{display:flex;align-items:center;gap:8px;margin-bottom:8px}
  .footer-rule{position:absolute;left:68px;right:68px;top:210px;border-top:1px solid var(--line)}
  .copyright{position:absolute;left:68px;top:225px;font-size:10px;color:var(--muted)}
  .socials{position:absolute;right:68px;top:218px;display:flex;gap:8px}
  .socials span{width:22px;height:22px;border:1.5px solid var(--red);border-radius:50%}
</style>
</head>
<body>
  <header class="hero">
    <div class="hero-photo" role="img" aria-label="Athlete training in a dark gym"></div>
    <div class="account">
      <svg width="9" height="9" viewBox="0 0 10 10"><circle cx="5" cy="3" r="2.2" fill="#fff"/><path d="M1 10a4 4 0 0 1 8 0z" fill="#fff"/></svg>
      Register / Login
    </div>
    <nav class="site-nav">
      <div class="brand">
        <div class="brand-name">VENTURE BRIGHTPATH</div>
        <div class="brand-by">by Marlon Tibbet</div>
      </div>
      <div class="nav-links">
        <span>About Us</span><span>Daily Workouts</span><span>Why Health and Wellness</span>
      </div>
      <span class="btn btn-contact">Contact</span>
    </nav>
    <h1 class="hero-title">FITNESS<br>PLANS</h1>
  </header>

  <main>
    <p class="intro">Pick the plan that fits your routine and get daily workouts, simple guidance and steady support from a coach who lives the way he teaches every single day.</p>

    <section class="plan" style="left:70px;top:362px">
      <h2>Basic</h2>
      <p class="sessions">4 sessions a month</p>
      <div class="price"><strong>$50</strong>per Session</div>
      <ul class="features">
        <li><svg width="8" height="7" viewBox="0 0 8 7"><path d="M1 3.5l2 2 4-4.5" stroke="#d6483b" stroke-width="1.5" fill="none"/></svg>Free consultation</li>
        <li><svg width="8" height="7" viewBox="0 0 8 7"><path d="M1 3.5l2 2 4-4.5" stroke="#d6483b" stroke-width="1.5" fill="none"/></svg>Bespoke training programme</li>
        <li><svg width="8" height="7" viewBox="0 0 8 7"><path d="M1 3.5l2 2 4-4.5" stroke="#d6483b" stroke-width="1.5" fill="none"/></svg>Weekly Check-ins</li>
        <li><svg width="8" height="7" viewBox="0 0 8 7"><path d="M1 3.5l2 2 4-4.5" stroke="#d6483b" stroke-width="1.5" fill="none"/></svg>Access to Direct Messages</li>
      </ul>
      <span class="btn btn-buy">Buy now</span>
    </section>

    <section class="plan featured" style="left:277px;top:356px">
      <h2>Advanced</h2>
      <p class="sessions">4 sessions a month</p>
      <div class="price"><strong>$200</strong>per Session</div>
      <ul class="features">
        <li><svg width="8" height="7" viewBox="0 0 8 7"><path d="M1 3.5l2 2 4-4.5" stroke="#d6483b" stroke-width="1.5" fill="none"/></svg>Free consultation</li>
        <li><svg width="8" height="7" viewBox="0 0 8 7"><path d="M1 3.5l2 2 4-4.5" stroke="#d6483b" stroke-width="1.5" fill="none"/></svg>Bespoke training programme</li>
        <li><svg width="8" height="7" viewBox="0 0 8 7"><path d="M1 3.5l2 2 4-4.5" stroke="#d6483b" stroke-width="1.5" fill="none"/></svg>Weekly Check-ins</li>
        <li><svg width="8" height="7" viewBox="0 0 8 7"><path d="M1 3.5l2 2 4-4.5" stroke="#d6483b" stroke-width="1.5" fill="none"/></svg>Access to Direct Messages</li>
        <li><svg width="8" height="7" viewBox="0 0 8 7"><path d="M1 3.5l2 2 4-4.5" stroke="#d6483b" stroke-width="1.5" fill="none"/></svg>Bespoke nutrition plans</li>
        <li><svg width="8" height="7" viewBox="0 0 8 7"><path d="M1 3.5l2 2 4-4.5" stroke="#d6483b" stroke-width="1.5" fill="none"/></svg>Exact calorie an macronutrients recommendations</li>
      </ul>
      <span class="btn btn-buy">Buy now</span>
    </section>

    <section class="plan" style="left:483px;top:362px">
      <h2>Advanced</h2>
      <p class="sessions">4 sessions a month</p>
      <div class="price"><strong>$270</strong>per Session</div>
      <ul class="features">
        <li><svg width="8" height="7" viewBox="0 0 8 7"><path d="M1 3.5l2 2 4-4.5" stroke="#d6483b" stroke-width="1.5" fill="none"/></svg>Free consultation</li>
        <li><svg width="8" height="7" viewBox="0 0 8 7"><path d="M1 3.5l2 2 4-4.5" stroke="#d6483b" stroke-width="1.5" fill="none"/></svg>Bespoke training programme</li>
        <li><svg width="8" height="7" viewBox="0 0 8 7"><path d="M1 3.5l2 2 4-4.5" stroke="#d6483b" stroke-width="1.5" fill="none"/></svg>Weekly Check-ins</li>
        <li><svg width="8" height="7" viewBox="0 0 8 7"><path d="M1 3.5l2 2 4-4.5" stroke="#d6483b" stroke-width="1.5" fill="none"/></svg>Access to Direct Messages</li>
        <li><svg width="8" height="7" viewBox="0 0 8 7"><path d="M1 3.5l2 2 4-4.5" stroke="#d6483b" stroke-width="1.5" fill="none"/></svg>Bespoke nutrition plans</li>
        <li><svg width="8" height="7" viewBox="0 0 8 7"><path d="M1 3.5l2 2 4-4.5" stroke="#d6483b" stroke-width="1.5" fill="none"/></svg>Exact calorie an macronutrients recommendations</li>
        <li><svg width="8" height="7" viewBox="0 0 8 7"><path d="M1 3.5l2 2 4-4.5" stroke="#d6483b" stroke-width="1.5" fill="none"/></svg>Additional check-ins available upon personal request</li>
        <li><svg width="8" height="7" viewBox="0 0 8 7"><path d="M1 3.5l2 2 4-4.5" stroke="#d6483b" stroke-width="1.5" fill="none"/></svg>1 Zone workout class per week</li>
      </ul>
      <span class="btn btn-buy">Buy now</span>
    </section>

    <section class="signup">
      <h2>SIGN UP FOR EXCLUSIVE CONTENT</h2>
      <span class="btn btn-register">Register</span>
    </section>
  </main>

  <footer class="site-footer">
    <div class="brand footer-brand">
      <div class="brand-name">VENTURE BRIGHTPATH</div>
      <div class="brand-by">by Marlon Tibbet</div>
    </div>
    <div class="footer-col links">
      <h3>Quick links</h3>
      <div>Home</div><div>About Us</div><div>Daily Workouts</div><div>Why Health and Wellness</div><div>Contact</div>
    </div>
    <div class="footer-col contact">
      <h3>Contact Us</h3>
      <p><svg width="10" height="10" viewBox="0 0 10 10"><path d="M2 1l2 2-1 1.2a6 6 0 0 0 2.8 2.8L7 6l2 2-1.3 1.3C4.5 9 1 5.5.7 2.3z" fill="#d6483b"/></svg>1 555 010 2040</p>
      <p><svg width="11" height="8" viewBox="0 0 11 8"><rect x=".5" y=".5" width="10" height="7" fill="none" stroke="#d6483b"/><path d="M.5.5l5 4 5-4" fill="none" stroke="#d6483b"/></svg>info@marlontibbet.com</p>
    </div>
    <div class="footer-rule"></div>
    <p class="copyright">© Venture Brightpath. All rights reserved.</p>
    <div class="socials"><span></span><span></span><span></span></div>
  </footer>
</body>
</html>
```